Biz Card & Stationary: Modern, boutique appeal for vacation rental company for high end luxury homes
Biz Card + Folder + Letterhead + Envelope
Simple
Marla Whitcombe
Owner
2817 Maple Hollow Ln Austin TX 78529
marla@quolbi.com
www.quolbi.com
-may create image or graphic to use with logo -Need letterhead & envelopes in word format

```html
<!DOCTYPE html>
<html lang="en">
<head>
<meta charset="utf-8">
<title>Quolbi Stays Business Card</title>
<link href="https://fonts.googleapis.com/css2?family=Raleway:wght@300;400;600&family=Oswald:wght@500&display=swap" rel="stylesheet">
<style>
  :root {
    --teal: #3dbfc8;
    --ink: #3f4346;
    --ink-soft: #6a6f73;
    --card: #ffffff;
    --bg-top: #e4e4e4;
    --bg-bottom: #cfcfcf;
  }
  * { box-sizing: border-box; margin: 0; padding: 0; }
  html, body { width: 1200px; height: 949px; overflow: hidden; }
  body {
    position: relative;
    background: linear-gradient(180deg, var(--bg-top), var(--bg-bottom));
    font-family: "Raleway", sans-serif;
    color: var(--ink);
  }
  .card {
    position: absolute;
    background: var(--card);
    border-radius: 22px;
    box-shadow: 0 14px 30px rgba(0,0,0,0.18);
  }
  .card-back { left: 440px; top: 60px; width: 640px; height: 366px; }
  .card-front { left: 120px; top: 470px; width: 700px; height: 400px; }

  .brand {
    position: absolute;
    font-family: "Raleway", sans-serif;
    font-weight: 300;
    color: var(--teal);
    letter-spacing: 1px;
    line-height: 1;
  }
  .card-back .brand { left: 150px; top: 130px; font-size: 72px; }
  .card-front .brand { left: 48px; top: 58px; font-size: 58px; }

  .social {
    position: absolute;
    right: 36px;
    bottom: 30px;
    display: flex;
    gap: 22px;
    font-size: 13px;
    color: var(--ink-soft);
  }
  .social-item { display: flex; align-items: center; gap: 7px; }
  .social-item i { width: 14px; height: 14px; background: var(--ink); display: block; }

  .identity {
    position: absolute;
    left: 420px;
    top: 50px;
    border-left: 4px solid var(--ink);
    padding-left: 14px;
  }
  .identity .name {
    font-family: "Oswald", sans-serif;
    font-weight: 500;
    font-size: 28px;
    letter-spacing: 1.5px;
    text-transform: uppercase;
    color: var(--ink);
  }
  .identity .role { font-size: 15px; color: var(--ink-soft); margin-top: 2px; }

  .contact-row {
    position: absolute;
    left: 60px;
    display: flex;
    align-items: center;
    gap: 24px;
  }
  .contact-row svg { width: 40px; height: 40px; flex: none; }
  .contact-row .lines {
    border-left: 3px solid var(--ink);
    padding-left: 14px;
    font-size: 17px;
    line-height: 1.5;
  }
  .row-phone { top: 180px; }
  .row-place { top: 252px; }
  .row-web { top: 324px; }
</style>
</head>
<body>
  <section class="card card-back">
    <div class="brand">quolbi stays</div>
    <div class="social">
      <span class="social-item"><i></i>/quolbistays</span>
      <span class="social-item"><i></i>@quolbistays</span>
    </div>
  </section>

  <section class="card card-front">
    <div class="brand">quolbi stays</div>
    <div class="identity">
      <div class="name">Marla Whitcombe</div>
      <div class="role">Managing Director</div>
    </div>

    <div class="contact-row row-phone">
      <svg viewBox="0 0 40 40" aria-hidden="true">
        <circle cx="20" cy="13" r="8" fill="var(--teal)"/>
        <path d="M5 37 C5 26 12 22 20 22 C28 22 35 26 35 37 Z" fill="var(--teal)"/>
      </svg>
      <div class="lines">512 555 0147<br>Landline 512 555 0102</div>
    </div>

    <div class="contact-row row-place">
      <svg viewBox="0 0 40 40" aria-hidden="true">
        <path d="M20 3 C12 3 7 9 7 16 C7 25 20 37 20 37 C20 37 33 25 33 16 C33 9 28 3 20 3 Z" fill="var(--teal)"/>
        <circle cx="20" cy="16" r="5" fill="#fff"/>
      </svg>
      <div class="lines">512 555 0183<br>marla@quolbi.com</div>
    </div>

    <div class="contact-row row-web">
      <svg viewBox="0 0 40 40" aria-hidden="true">
        <circle cx="20" cy="20" r="16" fill="var(--teal)"/>
        <g fill="none" stroke="#fff" stroke-width="1.8">
          <ellipse cx="20" cy="20" rx="7" ry="16"/>
          <line x1="4" y1="20" x2="36" y2="20"/>
          <line x1="7" y1="12" x2="33" y2="12"/>
          <line x1="7" y1="28" x2="33" y2="28"/>
          <line x1="20" y1="4" x2="20" y2="36"/>
        </g>
      </svg>
      <div class="lines">2817 Maple Hollow Ln<br>www.quolbi.com</div>
    </div>
  </section>
</body>
</html>
```